General Dental Office Business Card

I run a private general dental office in southern California, and would like a refresh/redesign of my business card. I focus on quality care rather than volume. The email address on the uploaded current card should be updated to: info@marbleshoredental.example. The current card's logo is a deboss, but I am open to other ideas. The logo can be refreshed, but it is something that's been with me since the beginning of the office, so I wouldn't want a drastic redesign.
Target Market(s)
Adults 18-99, whoever needs dental services
Industry/Entity Type
Healthcare/Dental
Contact Information for Business Card
Name, Address, Phone, email
Colors
Designer to choose colors to be used in the design.
Requirements
Must have
- Logo (Same as original one in the uploaded file), space on back for appointment time/date

```html
<!DOCTYPE html>
<html lang="en">
<head>
<meta charset="utf-8">
<title>Marble Shore Dental – Business Card</title>
<link rel="stylesheet" href="https://fonts.googleapis.com/css2?family=Raleway:wght@400;500;600;700&display=swap">
<style>
  :root {
    --backdrop: #9b9b9b;
    --card-white: #ffffff;
    --teal: #41b8c2;
    --teal-light: #6fcdd4;
    --teal-deep: #38aab4;
    --ink-grey: #6b6b6b;
    --rule-grey: #7a7a7a;
  }
  * { box-sizing: border-box; margin: 0; padding: 0; }
  html, body {
    width: 1200px; height: 1200px; overflow: hidden;
    background: var(--backdrop);
    font-family: "Raleway", sans-serif;
  }
  .card {
    position: absolute; left: 227px; width: 746px; height: 435px;
    border-radius: 26px; overflow: hidden;
  }
  .card--front { top: 120px; background: var(--card-white); }
  .card--back { top: 621px; background: var(--teal); }

  /* front */
  .brand {
    position: absolute; left: 40px; top: 150px; width: 300px;
    text-align: center; color: var(--teal);
  }
  .brand__dot {
    width: 110px; height: 110px; border-radius: 50%;
    border: 6px solid var(--teal); margin: 0 auto 18px;
  }
  .brand__name {
    font-weight: 500; font-size: 37px; line-height: 1.05; letter-spacing: 1px;
    text-transform: uppercase;
  }
  .brand { top: 108px; }
  .divider {
    position: absolute; left: 374px; top: 75px; width: 1.5px; height: 285px;
    background: var(--rule-grey);
  }
  .details { position: absolute; left: 424px; top: 78px; width: 300px; }
  .details__name { color: var(--teal); font-weight: 600; font-size: 28px; }
  .details__role { color: var(--ink-grey); font-size: 18px; margin-top: 2px; }
  .appt { margin-top: 26px; }
  .appt__row {
    display: flex; align-items: flex-end; color: var(--teal);
    font-size: 17px; font-weight: 500; height: 24px; margin-bottom: 20px;
  }
  .appt__line { flex: none; width: 190px; border-bottom: 1.5px solid var(--rule-grey); margin-left: 3px; margin-bottom: 4px; }
  .address { color: var(--ink-grey); font-size: 16px; line-height: 1.4; margin-top: 22px; padding-left: 4px; }
  .contact { margin-top: 14px; padding-left: 2px; }
  .contact__row { display: flex; align-items: center; color: var(--ink-grey); font-size: 16px; line-height: 1.5; }
  .contact__row svg { width: 16px; height: 16px; margin-right: 6px; fill: var(--teal); }

  /* back */
  .waves {
    position: absolute; left: 0; top: 0; width: 100%; height: 392px;
    background: repeating-linear-gradient(180deg, var(--teal-light) 0 12px, var(--teal) 12px 24px);
    opacity: .9;
  }
  .emblem {
    position: absolute; left: 236px; top: 56px; width: 274px; height: 274px;
    border-radius: 50%; border: 12px solid var(--card-white); background: var(--teal);
    display: flex; align-items: center; justify-content: center; text-align: center;
  }
  .emblem__name {
    color: var(--card-white); font-weight: 500; font-size: 32px; line-height: 1.15;
    text-transform: uppercase; letter-spacing: 1px;
  }
  .website {
    position: absolute; left: 0; right: 0; bottom: 8px; text-align: center;
    color: var(--card-white); font-weight: 600; font-size: 20px;
  }
</style>
</head>
<body>
  <section class="card card--front">
    <div class="brand">
      <div class="brand__dot"></div>
      <div class="brand__name">Marble Shore<br>Dental</div>
    </div>
    <div class="divider"></div>
    <div class="details">
      <div class="details__name">Dr. Elena Park</div>
      <div class="details__role">General Dentistry</div>
      <div class="appt">
        <div class="appt__row">Date:<span class="appt__line"></span></div>
        <div class="appt__row">Time:<span class="appt__line"></span></div>
      </div>
      <div class="address">1280 Harbor View Lane<br>Seacliff, CA 92000</div>
      <div class="contact">
        <div class="contact__row">
          <svg viewBox="0 0 24 24" aria-hidden="true"><path d="M6.6 10.8a15 15 0 0 0 6.6 6.6l2.2-2.2a1 1 0 0 1 1-.25 11.4 11.4 0 0 0 3.6.57 1 1 0 0 1 1 1V20a1 1 0 0 1-1 1A17 17 0 0 1 3 4a1 1 0 0 1 1-1h3.5a1 1 0 0 1 1 1c0 1.25.2 2.45.57 3.57a1 1 0 0 1-.25 1z"/></svg>
          (555) 014-2828
        </div>
        <div class="contact__row">
          <svg viewBox="0 0 24 24" aria-hidden="true"><path d="M2 5h20v14H2zm2 2v.4l8 5.2 8-5.2V7zm0 2.8V17h16V9.8l-8 5.2z"/></svg>
          info@marbleshoredental.example
        </div>
      </div>
    </div>
  </section>

  <section class="card card--back">
    <div class="waves" role="img" aria-label="Decorative pattern of light teal horizontal waves"></div>
    <div class="emblem"><div class="emblem__name">Marble Shore<br>Dental</div></div>
    <div class="website">www.marbleshoredental.example</div>
  </section>
</body>
</html>
```